Small animal veterinary clinic needs a new web site design

We need a new web site design for Harlowe Veterinary Clinic. The clinic performs medicine, surgery, and wellness care for cats and dogs. We have been in business for over 50 years so we want to project stability, reliability, class, elegance, and professionalism. We also want to convey that we have modern facilities and services and perform high quality medicine.
The current web site has been in place for many years and looks stale but for reference it is at http://www.harlowevc-example.com. We will be re-writing most of the content and looking to add additional pages, videos, downloadable documents (forms, brochures, marketing materials, etc.) The new owners prefer a more classy, modern look. Some vet clinic sites we like are http://pennfrolt.com and http://curaplumtails.com. We like a nice, clean, fresh, interactive interface.
Our new logo is attached. We want the color scheme of the web site to be complementary to the colors in the logo, especially the blue and green. The purple color of the text should just be used for accent. Upon request and if necessary, I can supply the Adobe Illustrator source file for the logo.
We are looking for a set of page designs - a great, eye-catching home page and 2-3 content page layouts we can use to create content pages with our own text and other content. Navigation design is very important as well. Again, we can fill in the content of the navigation links but I would like a nice, easy-to-use, logical navigation design. If you want some content or navigation links to use as reference during your design phase, feel free to pull whatever content or navigation you want from our existing web site. I am not looking for just images, I would like actual page files - HTML, CSS, etc.
Thanks and good luck!
Target Market(s)
We cater to pet owners across a wide age range. Socio-economic status of our customers is middle class and above. We do not target price shoppers.
Industry/Entity Type
Veterinary
Colors
Designer to choose colors to be used in the design.
Requirements
Must have
- Must look professional, clean, and modern. We are looking for simple but elegant design and navigation. 1 home page design, 2-3 content page designs delivered with code (HTML & CSS).
Nice to have
- When HTML/CSS is delivered, it would be awesome if it were mobile ready as well.
Should not have
- Colors that are too bold. Layout that is too complex.

```html
<!DOCTYPE html>
<html lang="en">
<head>
<meta charset="utf-8">
<title>Harlowe Veterinary Clinic</title>
<link rel="stylesheet" href="https://fonts.googleapis.com/css2?family=Roboto+Condensed:wght@400;700&family=Arimo:wght@400;700&family=Tinos&display=swap">
<style>
:root{
  --navy:#2b3790;
  --green:#3dba7c;
  --purple:#6c2b5e;
  --text:#7a7a7a;
  --dark:#4b4b4b;
  --footer:#5b5e63;
  --footer-text:#d9dadc;
  --line:#e2e2e2;
}
*{margin:0;padding:0;box-sizing:border-box}
html,body{width:906px;height:1200px;overflow:hidden;background:#fff}
body{position:relative;font-family:Arimo,Arial,sans-serif;color:var(--text)}
.abs{position:absolute}
.top-rule{left:0;top:0;width:906px;height:3px;background:var(--navy)}
.brand{left:99px;top:54px;display:flex;align-items:center;gap:6px;font-family:"Roboto Condensed",sans-serif;font-size:20px;font-weight:700;color:var(--navy);letter-spacing:1px}
.brand .dot{width:12px;height:12px;border-radius:50%;background:var(--green)}
.social{top:18px;display:flex;gap:7px;right:100px}
.social span{width:24px;height:24px;border:1.5px solid #b5b5b5;border-radius:50%}
.portal{top:64px;right:250px;font-family:"Roboto Condensed",sans-serif;font-size:11px;color:#555}
.btn{font-family:"Roboto Condensed",sans-serif;font-size:11px;color:#fff;display:flex;align-items:center;justify-content:center;border-radius:2px}
.btn-login{left:667px;top:58px;width:67px;height:25px;background:var(--navy)}
.btn-register{left:740px;top:58px;width:66px;height:25px;background:var(--green)}
.nav{left:99px;top:101px;width:708px;height:39px;background:var(--green);border-radius:3px}
.nav a{position:absolute;top:13px;font-family:"Roboto Condensed",sans-serif;font-size:11px;color:#fff;text-decoration:none}
.search{left:548px;top:5px;width:154px;height:29px;border:1px solid #fff;border-radius:2px;font-family:"Roboto Condensed",sans-serif;font-size:11px;color:#fff;padding:8px 10px}
.search svg{position:absolute;right:8px;top:7px}
.hero{left:99px;top:144px;width:708px;height:364px;background:linear-gradient(100deg,#c9d6de 0%,#d9b783 35%,#e8d2b0 55%,#d9a86a 80%,#b8c4cc 100%)}
.hero-caption{left:99px;top:466px;width:708px;height:42px;background:rgba(70,70,70,.72)}
.hero-caption p{position:absolute;left:13px;top:13px;font-family:Arimo,sans-serif;font-weight:700;font-size:14px;color:#fff;letter-spacing:.3px}
.arrow{top:477px;width:22px;height:22px;border-radius:50%;background:#fff;border:2px solid #555}
.arrow svg{display:block;margin:4px}
h2{position:absolute;font-family:"Roboto Condensed",sans-serif;font-weight:700;font-size:15px;color:var(--navy)}
.welcome-text{left:99px;top:556px;width:512px;font-size:8.6px;line-height:20.5px}
.read-more{left:99px;top:685px;width:80px;height:26px;background:var(--green);border-radius:2px;color:#fff;font-size:10px;display:flex;align-items:center;justify-content:center}
.welcome-photo{left:624px;top:512px;width:170px;height:194px;background:radial-gradient(ellipse at 50% 55%,#c9a679 0%,#7e8ba7 55%,#fff 78%)}
.staff{top:779px;width:225px}
.staff .photo{position:absolute;left:0;top:0;width:95px;height:83px;background:linear-gradient(135deg,#6d8a59,#b9a68f 50%,#47503f)}
.staff .name{position:absolute;left:106px;top:2px;font-family:"Roboto Condensed",sans-serif;font-weight:700;font-size:9.5px;color:var(--purple)}
.staff .role{position:absolute;left:106px;top:16px;font-family:"Roboto Condensed",sans-serif;font-style:italic;font-size:8.5px;color:var(--green)}
.staff .bio{position:absolute;left:106px;top:30px;width:120px;font-family:"Roboto Condensed",sans-serif;font-size:8.5px;line-height:14px}
.staff .more{position:absolute;left:0;top:88px;width:225px;font-family:"Roboto Condensed",sans-serif;font-size:8.5px;line-height:14px}
.staff .more b{font-weight:400;color:var(--green)}
.news{left:576px;width:230px}
.news .date{position:absolute;left:0;top:0;width:28px;height:27px;background:var(--green);color:#fff;font-family:"Roboto Condensed",sans-serif;font-size:9px;line-height:10px;text-align:center;padding-top:3px}
.news .title{position:absolute;left:35px;top:0;width:195px;font-family:"Roboto Condensed",sans-serif;font-size:10px;line-height:14px;color:var(--purple)}
.news .sum{position:absolute;left:0;top:36px;width:230px;font-size:8.3px;line-height:17px}
.news-rule{left:576px;top:853px;width:230px;height:1px;background:var(--line)}
.page-rule{left:99px;top:955px;width:708px;height:1px;background:var(--line)}
.footer{left:0;top:969px;width:906px;height:231px;background:var(--footer)}
.footer h3{position:absolute;font-family:Tinos,serif;font-weight:400;font-size:13px;color:#fff}
.footer .t{position:absolute;font-size:7.8px;color:var(--footer-text)}
.f-social{position:absolute;left:112px;display:flex;align-items:center;gap:12px;font-size:7.8px;color:#fff}
.f-social span{width:24px;height:24px;border:1.5px solid #a9abaf;border-radius:50%}
.bullet{position:absolute;font-size:7.8px;color:var(--footer-text);padding-left:10px}
.bullet::before{content:"";position:absolute;left:0;top:3px;width:4px;height:4px;border-radius:50%;background:#c8c9cc}
.f-brand{position:absolute;left:252px;top:162px;font-family:"Roboto Condensed",sans-serif;font-size:13px;color:#8e9196;letter-spacing:1px}
.guide .thumb{position:absolute;width:33px;height:30px;background:linear-gradient(135deg,#ddd,#8a7a66 60%,#444)}
.guide .txt{position:absolute;width:150px;font-size:7.8px;line-height:14px;color:var(--footer-text)}
.guide .txt b{font-weight:400;color:var(--green)}
.f-rule{position:absolute;left:112px;top:190px;width:682px;height:1px;background:#777a7f}
.copy{position:absolute;left:0;width:906px;top:210px;text-align:center;font-size:8px;color:var(--footer-text)}
</style>
</head>
<body>
<div class="abs top-rule"></div>

<header>
  <div class="abs brand"><span class="dot"></span>HARLOWE</div>
  <div class="abs social" aria-label="Social links"><span></span><span></span><span></span><span></span><span></span></div>
  <div class="abs portal">SIGN-IN TO YOUR PERSONALIZED PET PORTAL TODAY!</div>
  <div class="abs btn btn-login">LOGIN</div>
  <div class="abs btn btn-register">REGISTER</div>
  <nav class="abs nav">
    <a style="left:19px">OUR PRACTICE</a>
    <a style="left:121px">SERVICES</a>
    <a style="left:202px">OUR STAFF</a>
    <a style="left:289px">CARE GUIDES</a>
    <a style="left:385px">CONTACT US</a>
    <a style="left:479px">MORE INFO</a>
    <div class="abs search">SEARCH
      <svg width="14" height="14" viewBox="0 0 14 14"><circle cx="5.5" cy="5.5" r="4" fill="none" stroke="#fff" stroke-width="2"/><line x1="8.5" y1="8.5" x2="12.5" y2="12.5" stroke="#fff" stroke-width="2.4"/></svg>
    </div>
  </nav>
</header>

<section>
  <div class="abs hero" role="img" aria-label="Veterinarian smiling with a golden retriever puppy"></div>
  <div class="abs hero-caption"><p>MEDICINE,SURGERY,&amp; WELLNESS CARE &nbsp;FOR &nbsp;CATS AND DOGS</p></div>
  <div class="abs arrow" style="left:744px"><svg width="10" height="10" viewBox="0 0 10 10"><path d="M7 1 3 5l4 4" fill="none" stroke="#444" stroke-width="2.2"/></svg></div>
  <div class="abs arrow" style="left:773px"><svg width="10" height="10" viewBox="0 0 10 10"><path d="M3 1l4 4-4 4" fill="none" stroke="#444" stroke-width="2.2"/></svg></div>
</section>

<section>
  <h2 style="left:99px;top:526px">WELCOME TO OUR COMPANY</h2>
  <p class="abs welcome-text">Harlowe Veterinary Clinic is a full-service veterinary medical hospital, located in Brennford, SC. The professional and courteous staff at Harlowe Veterinary Clinic seeks to provide the best possible medical care, surgical care and dental care for their highly-valued.Harlowe Veterinary Clinic is a full-service veterinary medical hospital, located in Brennford, SC. The professional and courteous staff at Harlowe Veterinary Clinic seeks to provide the best possible medical care, surgical care and dental care for their highly-valued...Harlowe Veterinary Clinic is a full-service veterinary medical hospital, located in Brennford, SC. The professional and highly-valued.Harlowe Veterinary Clinic......</p>
  <div class="abs read-more">READ MORE</div>
  <div class="abs welcome-photo" role="img" aria-label="Young woman kneeling with a golden retriever"></div>
</section>

<section>
  <h2 style="left:99px;top:741px">OUR STAFF</h2>
  <div class="abs staff" style="left:99px">
    <div class="photo" role="img" aria-label="Veterinarian holding a small dog outdoors"></div>
    <div class="name">MARIAN L. CORWELL, D.V.M.</div>
    <div class="role">Owner / Veterinarian</div>
    <div class="bio">Dr. Marian Corwell received her BS (cum laude) in Biology from The University of Carrowmead The University of Eastvale.....</div>
    <div class="more">Dr. Harlowe. &nbsp;In 1984 they purchased the practice from Dr. Harlowe, retaining the name of Harlowe Veterinary Clinic. &nbsp;Born in Lindale, SC and raised in Ashcroft, GA, Dr. Marian was "coming home"........<b>READ MORE</b></div>
  </div>
  <div class="abs staff" style="left:342px">
    <div class="photo" role="img" aria-label="Veterinarian with two dogs"></div>
    <div class="name">MARIAN L. CORWELL, D.V.M.</div>
    <div class="role">Owner / Veterinarian</div>
    <div class="bio">Dr. Marian Corwell received her BS (cum laude) in Biology from The University of Carrowmead The University of Eastvale.....</div>
    <div class="more">Dr. Harlowe. &nbsp;In 1984 they purchased the practice from Dr. Harlowe, retaining the name of Harlowe Veterinary Clinic. &nbsp;Born in Lindale, SC and raised in Ashcroft, GA, Dr. Marian was "coming home"........<b>READ MORE</b></div>
  </div>

  <h2 style="left:576px;top:741px">LATEST NEWS</h2>
  <div class="abs news" style="top:777px">
    <div class="date">24<br>Jun</div>
    <div class="title">Neque porro quisquam est qui dolorem ipsum quia dolor sit amet, consectetur....</div>
    <div class="sum">Sed ut perspiciatis unde omnis iste natus error sit voluptatem accusantium doloremque laudantium.........</div>
  </div>
  <div class="abs news-rule"></div>
  <div class="abs news" style="top:866px">
    <div class="date">24<br>Jun</div>
    <div class="title">Neque porro quisquam est qui dolorem ipsum quia dolor sit amet, consectetur....</div>
    <div class="sum">Sed ut perspiciatis unde omnis iste natus error sit voluptatem accusantium doloremque laudantium.........</div>
  </div>
  <div class="abs page-rule"></div>
</section>

<footer class="abs footer">
  <h3 style="left:112px;top:20px">Follow Us :</h3>
  <div class="f-social" style="top:53px"><span></span>Pawbook</div>
  <div class="f-social" style="top:83px"><span></span>Chirper</div>
  <div class="f-social" style="top:111px"><span></span>Linkwork</div>
  <div class="f-social" style="top:138px"><span></span>Pinboard</div>

  <h3 style="left:239px;top:20px">links</h3>
  <div class="bullet" style="left:240px;top:52px">Tallow Kibble</div>
  <div class="bullet" style="left:240px;top:73px">Please visit our website for Boarding</div>
  <div class="bullet" style="left:240px;top:93px">and Grooming</div>
  <div class="f-brand">HARLOWE</div>

  <h3 style="left:411px;top:20px">Care Guides</h3>
  <div class="guide">
    <div class="thumb" style="left:411px;top:53px" role="img" aria-label="Owner exercising with a dog"></div>
    <div class="txt" style="left:453px;top:54px"><b>Exercising Your Dog</b>BrightPath engage-ments begin with awith your team.......</div>
    <div class="thumb" style="left:411px;top:97px" role="img" aria-label="Veterinarian examining a cat"></div>
    <div class="txt" style="left:453px;top:98px"><b>Feline Obesity</b>BrightPath engagements begin with a discussion with team......</div>
    <div class="thumb" style="left:411px;top:141px" role="img" aria-label="Veterinarian with a pet"></div>
    <div class="txt" style="left:453px;top:141px"><b>Spaying or Neutering Your Pet</b>BrightPath engagements begin &nbsp;with your team.......</div>
  </div>

  <h3 style="left:635px;top:22px">Location</h3>
  <div class="t" style="left:633px;top:57px">Feel free to contact us if you have any problems.</div>
  <div class="bullet" style="left:635px;top:78px">Address :The Maplane map is incorrect</div>
  <div class="t" style="left:638px;top:99px">1 &nbsp;482 East 9th Ridge Street</div>
  <div class="bullet" style="left:635px;top:119px">Email : &nbsp;support@harlowevc-example.com</div>
  <div class="bullet" style="left:635px;top:140px">Phone : &nbsp;(555) 014-2761</div>
  <div class="bullet" style="left:635px;top:160px">Fax: (555) 014-0127</div>

  <div class="f-rule"></div>
  <div class="copy">© Copy Rights &nbsp;2014 - Harlowe VC .All rights reserved</div>
</footer>
</body>
</html>
```